Cruise price comparison web design project

The project's name is Wellenfuchsportal.
www.wellenfuchsportal.de
The current design (which I don't really like) can be found here:
http://wfp02.wellenfuchsportal.de/

I m not too happy with what the current developers have been done so far (in terms of design), so I hope to find a great designer her to develop a design that kicks arses. : )

We are currently developing a site for the German market that brings travel agents and cruise holiday makers together. We are not an ordinary travel agency.
Wellenfuchsportal is a quick and convenient way to have independent travel agencies compete to offer our site visitors the best cruise deal available in Europe.

Here is a short video that explains what one of our competitors does; it gives a good overview as our site will be similar:
http://www.voyabidder.com/video_how_voyabidder_works.php
(Voyabidder.com is not a great website in terms of design, so please dont get me wrong.)

The logo has already been created, but both the colours (should remain blueish) and the font can be modified. The font colour can be changed dramatically if you think this is of advantage.

The Website design should be professional and unique and become an eye catcher. It must attract visitors of all age groups, a "wow-effect" is definitely a bonus.
Users should easily see what this website is about.

We need the following text on our homepage:

"Immer der beste Preis -
denn Reisebüros kämpfen um Sie!"
(means "Always the best rate - as travel agents compete offer the best deal")
This is a sort of headline.

We also need:

So funktioniert Wellenfuchsportal:
1. Wunschkreuzfahrt wählen
2. Angebote erhalten und vergleichen
3. Reisebüro kontaktieren und buchen

(This explains briefly how our system works.)

Aside banners maybe needed later for advertising.

Additions I need on the front page are:
- Login / Sign-Up / Your benefits
(I quite like the way it's done on http://www.lirmatimes.com, at the very top of the page)
- Recommendation-link
(for everything else: Pls. refer to wfp02.wellenfuchsportal.de
- 3 or 4 "top offers of the week"
(current format is not very appealing; offers can be displayed as on http://sailings.tripnuvo.com/affiliate/promo.rvlx?OfferID=DOLUMA27 or

A maritime look is surely an option here, as we focus on cruises. But maybe you can surprise me with a great idea.

I quite like the designs where basically one photo / picture is used.
Some examples which look great IMHO:
http://pell-works.artfolioz.com/art/Glint-Swimmers-519304826
http://quorvanwebdesign.artfolioz.com/art/Website-Design-736152940
The following designer has also done a great job:
http://pixelmaker4387.artfolioz.com/gallery/

ATTACHED:
- logo
- Glint-Swimmers Design .png
- Flyer we use to attract travel agencies
- photo we use for the flyer (we own the rights)

Please get in touch with me if there are any questions or if you require further details. I ll get back to all inquiries / messages as soon as possible, usually within a few hours... Feel free to ask technical questions, too, (if any), the developer will be of assistance.

Reason: I decided to extend the deadline to have more time to comment on your designs and allow you to submit a few more proposals.

Reason: Sorry, more time needed to comment on all designs. Apart from this, some designers asked for more time.

Dear All,

Thank you so much for all your proposals.
Later today I will have a decent internet connection connection again, so I will be able to finally comment on your ideas and visions.

Hopefully next week we can finalize this project. Feel free to submit more designs or ask any questions if there are any.
Remember: Wellenfuchsportal won't be an ordinary travel agent. It brings cruise holiday makers and travel agents together.

Best

Target Market(s)

Holidaymakers / potential cruise holiday makers between 20 and 80.

Industry/Entity Type

Advertising

Requirements
Should not have
• Design should not use old-style, serif fonts.

```html
<!DOCTYPE html>
<html lang="de">
<head>
<meta charset="utf-8">
<title>Wellenfuchsportal – Kreuzfahrt-Angebote</title>
<link rel="stylesheet" href="https://fonts.googleapis.com/css2?family=Questrial&family=Gelasio:wght@400&display=swap">
<style>
:root{
  --sea-deep:#0f4a4a;
  --sea-mid:#3d8f86;
  --sea-light:#b9e6d6;
  --sky:#d8efe6;
  --panel:rgba(190,235,215,.82);
  --panel-edge:rgba(255,255,255,.55);
  --nav:#2c6b62;
  --nav-active:#8ccf5c;
  --green:#8cc84f;
  --red:#a8151b;
  --ink:#3f5a55;
  --white:#ffffff;
  --footer:rgba(20,55,55,.55);
}
*{box-sizing:border-box;margin:0;padding:0}
html,body{width:852px;height:1200px;overflow:hidden}
body{position:relative;font-family:"Questrial",sans-serif;color:var(--ink);background:var(--sea-deep)}
.scene{position:absolute;inset:0;
  background:
   radial-gradient(ellipse 300px 220px at 530px 120px,rgba(255,255,240,.7),transparent 70%),
   radial-gradient(ellipse 380px 120px at 430px 400px,rgba(235,250,245,.9),transparent 75%),
   radial-gradient(ellipse 200px 260px at 90px 260px,rgba(110,130,40,.75),transparent 70%),
   linear-gradient(180deg,#2e7f80 0%,#8ec9b9 18%,#cfeee0 35%,#9fd6c4 48%,#6db5a4 62%,#3d8075 78%,#274f43 100%)}
.login-bar{position:absolute;left:0;top:0;width:240px;height:15px;background:#eef3f1;border-radius:0 0 6px 0;display:flex;gap:18px;padding-left:97px;font-size:8.5px;line-height:15px;color:#444}
.contact{position:absolute;right:32px;top:5px;text-align:right;color:var(--white)}
.contact-label{font-family:"Gelasio",serif;font-size:9px}
.contact-phone{font-size:22px;letter-spacing:.5px;line-height:22px}
.social{display:flex;gap:5px;justify-content:flex-end;margin-top:6px}
.social span{width:17px;height:17px;border-radius:3px;background:rgba(255,255,255,.75)}
.brand{position:absolute;left:225px;top:60px;display:flex;align-items:center;gap:10px;color:var(--white);font-family:"Gelasio",serif;font-size:24px}
.brand-mark{width:34px;height:34px;border-radius:50%;background:var(--white)}
.tagline{position:absolute;left:503px;top:120px;font-family:"Gelasio",serif;font-size:16.5px;line-height:19px;color:#24504c}
.nav{position:absolute;left:94px;top:466px;width:666px;height:38px;background:var(--nav);border-radius:4px;display:flex;align-items:center;padding-left:8px;font-size:12px;color:var(--white);box-shadow:0 2px 4px rgba(0,0,0,.3);overflow:hidden}
.nav a{padding:0 5px;height:34px;line-height:34px;text-decoration:none;color:inherit;white-space:nowrap}
.nav a.active{background:var(--nav-active);border-radius:3px}
.panel{position:absolute;background:var(--panel);border:1px solid var(--panel-edge);border-radius:3px;box-shadow:0 1px 3px rgba(0,0,0,.2)}
.how{left:94px;top:516px;width:217px;height:158px;padding:21px 10px}
.panel-title{font-family:"Gelasio",serif;font-size:11.5px;color:#333;margin-bottom:16px;white-space:nowrap}
.steps{list-style:none}
.steps li{display:flex;align-items:center;gap:6px;font-family:"Gelasio",serif;font-size:10.5px;color:#333;margin-bottom:13px;white-space:nowrap}
.step-num{flex:none;width:21px;height:21px;border-radius:50%;background:linear-gradient(#e8f8f2,#7fc2ad);color:var(--white);font-size:12px;display:flex;align-items:center;justify-content:center;box-shadow:0 1px 2px rgba(0,0,0,.3)}
.ads{left:94px;top:682px;width:217px;height:244px;padding:16px 13px}
.ad-slot{width:174px;height:53px;margin:0 auto 8px;background:linear-gradient(#f7fbfa,#dce9e5);border:1px solid #b9cbc6;border-radius:3px}
.ads .panel-title{font-size:12.5px}
.deals-head{position:absolute;left:317px;top:516px;width:443px;height:34px;background:rgba(30,80,70,.85);border-radius:3px;padding:3px 9px;color:#bfe58d;font-size:11.5px;line-height:13px;letter-spacing:.6px}
.deals-head small{display:block;font-size:10px;color:#9fcf6d}
.offer{left:317px;width:443px;height:118px;padding:2px 9px;overflow:hidden}
.offer-title{font-size:13px;color:#4e6a63;margin-bottom:5px}
.offer-photo{position:absolute;left:9px;top:25px;width:133px;height:83px;background:linear-gradient(180deg,#8fb4cc 0%,#d9e3e6 55%,#50707e 100%);box-shadow:0 1px 2px rgba(0,0,0,.3)}
.offer-info{position:absolute;left:157px;top:30px;font-size:10px;line-height:12px;color:#6b7d78;width:150px}
.offer-info .hl{color:var(--red)}
.price{position:absolute;left:307px;top:60px;color:var(--red);font-size:16px;line-height:16px}
.price small{display:block;font-size:10px}
.order{position:absolute;left:306px;top:92px;width:130px;height:22px;border-radius:4px;background:linear-gradient(#fff,#dfe8e5);border:1px solid #b8c6c2;font-size:11px;color:#333;text-align:center;line-height:20px}
.order.hover{background:linear-gradient(#fff,#cfe7a8)}
.ribbon{position:absolute;right:-24px;top:18px;width:110px;height:17px;background:var(--green);color:#2f4a1e;font-size:7px;line-height:17px;text-align:center;transform:rotate(45deg)}
.more{position:absolute;left:524px;top:930px}
.footer{position:absolute;left:94px;top:958px;width:666px;height:102px;background:var(--footer);border-top:1px solid rgba(255,255,255,.4);padding-top:12px;display:grid;grid-template-columns:179px 216px 139px 1fr;color:var(--white);font-size:8.5px;line-height:15.6px}
.footer h3{font-weight:400;font-size:11px;margin-bottom:3px}
.footer .col:first-child{padding-left:3px}
.rule{position:absolute;left:132px;top:1111px;width:588px;border-top:1px solid rgba(255,255,255,.35)}
.about{position:absolute;left:0;right:0;top:1126px;text-align:center;color:var(--white);font-size:8px;line-height:12.5px}
</style>
</head>
<body>
<div class="scene" role="img" aria-label="Tropisches Meerpanorama mit Felsküste, Wolken, Kreuzfahrtschiff in der Gischt und Unterwasserriff"></div>

<nav class="login-bar"><span>Login</span><span>Sign-Up</span><span>Your benefits</span></nav>

<div class="contact">
  <div class="contact-label">Mit Kreuzfahrt-Experten Sprechen</div>
  <div class="contact-phone">04821-593027</div>
  <div class="social"><span></span><span></span><span></span><span></span></div>
</div>

<div class="brand"><span>Wellenfuchsportal</span><span class="brand-mark"></span></div>
<p class="tagline">Immer der beste Preis<br>denn Reisebüros kämpfen um Sie!</p>

<nav class="nav">
  <a>So Gehts</a><a class="active">Angebote erhalten</a><a>Kreuzfahrtsuche</a><a>Reedereien und Schiffe</a><a>Specials</a><a>Kontakt</a><a>Fehlermeldung</a><a>Trac</a>
</nav>

<section class="panel how">
  <h2 class="panel-title">So funktioniert Wellenfuchsportal:</h2>
  <ol class="steps">
    <li><span class="step-num">1</span>Wunschkreuzfahrt wählen</li>
    <li><span class="step-num">2</span>Angebote erhalten und vergleichen</li>
    <li><span class="step-num">3</span>Reisebüro kontaktieren und buchen</li>
  </ol>
</section>

<aside class="panel ads">
  <h2 class="panel-title">Advertising Area</h2>
  <div class="ad-slot"></div><div class="ad-slot"></div><div class="ad-slot"></div>
</aside>

<header class="deals-head">Finden Sie Ihr Kreuzfahrt-Schnäppchen!<small>Hier finden Sie wochenaktuell eine Auswahl der attraktivsten Kreuzfahrt-Angebote</small></header>

<article class="panel offer" style="top:556px">
  <h3 class="offer-title">Von der Stadt des Tangos zum Big Apple</h3>
  <div class="offer-photo" role="img" aria-label="Kreuzfahrtschiff auf dem Meer"></div>
  <p class="offer-info"><span class="hl">Inkl. Flügen mit Aerolinda,<br>Transfers &amp; Hotelübernachtung<br>in Buenos Aires</span><br>22 Tage Südamerika<br>Kreuzfahrt<br>Termin <span class="hl">Juli 2012</span></p>
  <p class="price">ab € 2.899<small>Pro Person</small></p>
  <div class="order">Angebot bestellen</div>
  <div class="ribbon">Serenity of the Waves</div>
</article>

<article class="panel offer" style="top:682px">
  <h3 class="offer-title">Rund um Island - ab/bis Hamburg</h3>
  <div class="offer-photo" role="img" aria-label="Promenadendeck eines Schiffes mit Blick aufs Meer" style="background:linear-gradient(180deg,#6f8ea6,#c9c3b3 70%,#8a7a66)"></div>
  <p class="offer-info"><span class="hl">Top-Angebot</span><br>12 Tage Island Kreuzfahrt<br>Termin <span class="hl">26.Juni 2012</span></p>
  <p class="price" style="top:56px">ab € 1.300<small>Pro Person</small></p>
  <div class="order hover">Angebot bestellen</div>
  <div class="ribbon">Legacy of the Waves</div>
</article>

<article class="panel offer" style="top:808px">
  <h3 class="offer-title">Von der Stadt des Tangos zum Big Apple</h3>
  <div class="offer-photo" role="img" aria-label="Kreuzfahrtschiff auf dem Meer"></div>
  <p class="offer-info"><span class="hl">Inkl. Flügen mit Aerolinda,<br>Transfers &amp; Hotelübernachtung<br>in Buenos Aires</span><br>22 Tage Südamerika<br>Kreuzfahrt<br>Termin <span class="hl">Juli 2012</span></p>
  <p class="price">ab € 2.899<small>Pro Person</small></p>
  <div class="order">Angebot bestellen</div>
  <div class="ribbon">Serenity of the Waves</div>
</article>

<svg class="more" width="28" height="12" viewBox="0 0 28 12"><path d="M2 2 L14 9 L26 2" fill="none" stroke="#d8f0e6" stroke-width="3"/></svg>

<footer class="footer">
  <div class="col"><h3>Über uns</h3>Über Wellenfuchsportal.de<br>Jobs<br>Partner<br>Werbung auf Wellenfuchsportal.de</div>
  <div class="col"><h3>Presse</h3>Pressematerial<br>Wellenfuchsportal in den Medien<br>Pressemitteilungen<br>Wellenfuchsportal und die Sozialen Medien</div>
  <div class="col"><h3>Hilfe &amp; Service</h3>Kundenmeinungen<br>Kontakt<br>FAQ's</div>
  <div class="col"><h3>Rechtliches</h3>Disclaimer / Haftungsausschluss<br>Nutzungsbedingungen.<br>Impressum</div>
</footer>

<div class="rule"></div>
<p class="about">Wellenfuchsportal.de ist ein völlig neuer Service, welcher Sie schnell und bequem den günstigsten Preis für eine Kreuzfahrt finden lässt.<br>Lange Suchen nach preiswerten Kreuzfahrten gehören ab sofort der Vergangenheit an, denn Reisebüros kämpfen um Sie.<br>Sparen Sie bares Geld und testen Sie Wellenfuchsportal.de – natürlich völlig kostenlos. Finden Sie Ihr Kreuzfahrt-Schnäppchen!<br>Zuletzt aktualisiert: 30.11.2012 | © 2010-2012 Wellenfuchsportal.de</p>
</body>
</html>
```